New ideas for home page of my website

I am looking for some inspiration for my website www.crafthollowworks.com
Most of the content will stay the same but I will be adding on the following new buttons Annual Expo and Awards
Any ideas on alternative layout act will be great. The most creative idea will get the opportunity to pitch for the whole site design.

Colors

Designer to choose colors to be used in the design.

```html
<!DOCTYPE html>
<html lang="en">
<head>
<meta charset="utf-8">
<title>Craft Hollow Works – Home</title>
<link href="https://fonts.googleapis.com/css2?family=Open+Sans:wght@400;600;700&display=swap" rel="stylesheet">
<style>
:root{
  --red:#c8102e;
  --ink:#333;
  --muted:#9a9a9a;
  --line:#e2e2e2;
  --nav-bg:#eeeff1;
  --band:#dde3ec;
  --footer:#2d2d2d;
  --footer-deep:#222;
  --star:#2f8ad8;
  --star-off:#c9c9c9;
  --white:#fff;
}
*{box-sizing:border-box;margin:0;padding:0}
html,body{width:689px;height:1200px;overflow:hidden}
body{position:relative;background:var(--white);font-family:'Open Sans',Arial,sans-serif;color:var(--ink)}
.abs{position:absolute}

/* header */
.site-header{left:0;top:0;width:689px;height:67px}
.brand{left:78px;top:12px;display:flex;align-items:center;gap:8px}
.brand-mark{width:40px;height:40px;border-radius:50%;background:var(--red)}
.brand-name{font-size:15px;font-weight:700;color:var(--red);line-height:1;width:90px}
.search{left:384px;top:25px;width:144px;height:22px;border:1px solid #d6d6d6;font-size:9px;color:#aaa;padding:5px 6px}
.search svg{position:absolute;right:6px;top:5px}
.lang{left:535px;top:25px;width:86px;height:22px;background:#2f2f2f;color:#fff;font-size:9px;padding:5px 7px}
.lang svg{position:absolute;right:8px;top:8px}

/* nav */
.main-nav{left:0;top:67px;width:689px;height:28px;background:var(--nav-bg)}
.main-nav ul{list-style:none;display:flex;position:absolute;left:70px;top:0;height:28px}
.main-nav li{font-size:7.5px;text-transform:uppercase;padding:0 10px;line-height:28px;border-right:1px solid #dcdde0;color:#444}
.main-nav li.active{background:#fff;border-bottom:2px solid var(--red);padding:0 15px}

/* hero */
.hero{left:0;top:95px;width:689px;height:169px;background:radial-gradient(ellipse at 40% 50%,#6b6b6b 0%,#3e3e3e 55%,#262626 100%)}
.hero-title{left:123px;top:136px;color:#fff;font-size:15px;font-weight:400;line-height:19px}
.hero-btn{left:125px;top:190px;width:92px;height:22px;border:2px solid #ddd;color:#fff;font-size:8.5px;text-align:center;line-height:18px}
.login{left:418px;top:119px;width:148px;height:121px;background:rgba(235,235,235,.95);padding:12px 15px}
.login h2{font-size:8px;font-weight:700;letter-spacing:.3px;margin-bottom:6px;color:#333}
.login .field{height:20px;background:#fff;border:1px solid #ccc;font-size:7px;padding:5px 6px;margin-bottom:7px;color:#444}
.login .row{display:flex;justify-content:space-between;align-items:center;font-size:6px;color:#333}
.login .btn{background:var(--red);color:#fff;font-size:7px;font-weight:600;width:40px;height:20px;line-height:20px;text-align:center}

/* section headings */
.section-title{top:295px;font-size:11px;font-weight:400;padding-bottom:6px;border-bottom:1px solid var(--line);height:23px}
.section-title b{color:var(--red);font-weight:700}

/* cards */
.card{border:1px solid var(--line);background:#fff}
.card-media{width:100%}
.card-body{padding:8px 10px 0}
.card-body h3{font-size:9px;font-weight:400;color:#444}
.card-body .cat{font-size:7px;color:var(--muted);margin-top:2px}
.card-body .desc{font-size:6px;color:var(--muted);line-height:8.5px;margin-top:10px}
.card-foot{position:absolute;left:0;bottom:0;width:100%;height:22px;border-top:1px solid var(--line);display:flex;align-items:center;padding:0 7px;gap:6px;font-size:7px;color:#555}
.stars{color:var(--star);font-size:10px;letter-spacing:-1px}
.stars span{color:var(--star-off)}
.fb{width:10px;height:10px;border-radius:50%;background:#cfcfcf;margin-left:6px}
.retrip{display:flex;align-items:center;gap:4px}

.loading{border:1px solid var(--line);background:#fff;text-align:center;font-size:9px;color:#666;padding-top:14px}
.loading svg{display:block;margin:0 auto 3px}

.followers{padding:10px 13px}
.followers h3{font-size:9.5px;font-weight:400;color:#555;margin-bottom:9px}
.follower{display:flex;align-items:center;gap:8px;height:37px}
.avatar{width:26px;height:26px;border-radius:50%;background:linear-gradient(#8a8a8a,#4a4a4a)}
.follower .name{font-size:8px;color:#444}
.follower .place{font-size:6px;color:var(--muted)}
.view-all{position:absolute;right:12px;bottom:10px;font-size:7px;color:#555}

/* band */
.band{left:0;top:902px;width:689px;height:202px;background:var(--band)}
.band-title{left:0;width:689px;text-align:center;font-size:8.5px;color:#555}
.band-title::before,.band-title::after{content:"";display:inline-block;width:150px;height:1px;background:#c8cfd9;vertical-align:middle;margin:0 10px}
.carousel{left:70px;top:936px;width:551px;height:52px;background:#eef0f3}
.carousel svg.arrow{position:absolute;top:18px}
.member{position:absolute}
.partner{position:absolute;background:#c9ced6;height:22px}

/* footer */
.site-footer{left:0;top:1104px;width:689px;height:72px;background:var(--footer);text-align:center;color:#ddd}
.site-footer .stats{font-size:8.5px;font-weight:700;margin-top:12px;line-height:13px}
.site-footer nav{font-size:6.5px;margin-top:7px;display:flex;justify-content:center;gap:8px;color:#bbb}
.site-footer nav .current{color:#fff}
.bottom-bar{left:0;top:1176px;width:689px;height:24px;background:var(--footer-deep);color:#bbb;font-size:6.5px;display:flex;justify-content:center;align-items:center;gap:8px}
.social{width:12px;height:12px;border-radius:50%;background:#bbb;display:inline-block}
</style>
</head>
<body>

<header class="site-header abs">
  <div class="brand abs"><span class="brand-mark"></span><span class="brand-name">CRAFT HOLLOW WORKS</span></div>
  <div class="search abs">Search here
    <svg width="10" height="10" viewBox="0 0 10 10"><circle cx="4" cy="4" r="3.2" fill="none" stroke="#aaa" stroke-width="1.2"/><line x1="6.4" y1="6.4" x2="9.3" y2="9.3" stroke="#aaa" stroke-width="1.2"/></svg>
  </div>
  <div class="lang abs">Language
    <svg width="9" height="6" viewBox="0 0 9 6"><path d="M1 1l3.5 3.5L8 1" fill="none" stroke="#fff" stroke-width="1.2"/></svg>
  </div>
</header>

<nav class="main-nav abs">
  <ul>
    <li class="active">Home</li><li>Learn More</li><li>News</li><li>Events</li><li>Members</li><li>Annual Expo</li><li>Awards</li><li>Council</li>
  </ul>
</nav>

<section class="hero abs" role="img" aria-label="Close-up of dark industrial machinery gears"></section>
<h1 class="hero-title abs">Championing World class<br>industry in the Midlands</h1>
<div class="hero-btn abs">Become a Member</div>
<form class="login abs">
  <h2>LOGIN HERE :</h2>
  <div class="field">Email Address</div>
  <div class="field">Password</div>
  <div class="row"><span>Forgotten Password?</span><span class="btn">Login</span></div>
</form>

<h2 class="section-title abs" style="left:70px;width:269px"><b>Featured</b> Article</h2>
<h2 class="section-title abs" style="left:348px;width:131px"><b>Latest</b> News</h2>
<h2 class="section-title abs" style="left:491px;width:131px"><b>Upcoming</b> Events</h2>

<!-- row 1 -->
<article class="card abs" style="left:70px;top:331px;width:129px;height:231px">
  <div class="card-media" style="height:128px;background:linear-gradient(135deg,#0e3e5a,#2aa6c9 55%,#0c2a3c)" role="img" aria-label="Glowing microchip on a circuit board"></div>
  <div class="card-body"><h3>Rio - Movie</h3><p class="cat">Wallpapers</p><p class="desc">Lorem Ipsum is simply dummy text of the printing &amp; typesetting industry.</p></div>
  <div class="card-foot"><span class="stars">★★★<span>★</span></span><span class="fb"></span><span class="retrip"><svg width="8" height="7" viewBox="0 0 8 7"><rect x="1" y="1" width="6" height="5" fill="none" stroke="#777"/></svg>Retrip</span></div>
</article>
<article class="card abs" style="left:210px;top:331px;width:129px;height:227px">
  <div class="card-media" style="height:163px;background:linear-gradient(160deg,#5a4a36,#8a6c4a 50%,#2d2a26)" role="img" aria-label="Factory worker in a cap in a workshop"></div>
  <div class="card-body"><h3>Kids movie -Kunfu</h3><p class="cat">Video clips</p></div>
  <div class="card-foot"><span class="stars">★★★<span>★</span></span><span class="fb"></span><span class="retrip"><svg width="8" height="7" viewBox="0 0 8 7"><rect x="1" y="1" width="6" height="5" fill="none" stroke="#777"/></svg>Retrip</span></div>
</article>
<article class="card abs" style="left:350px;top:331px;width:129px;height:227px">
  <div class="card-media" style="height:123px;background:linear-gradient(135deg,#e9e6e0,#b8b2aa 60%,#3b3f4a)" role="img" aria-label="Businessman in a suit in an office"></div>
  <div class="card-body"><h3>Kungfu - Movie</h3><p class="cat">Wallpapers</p><p class="desc">Lorem Ipsum is simply dummy text of the printing &amp; typesetting industry.</p></div>
  <div class="card-foot"><span class="stars">★★★<span>★</span></span><span class="fb"></span><span class="retrip"><svg width="8" height="7" viewBox="0 0 8 7"><rect x="1" y="1" width="6" height="5" fill="none" stroke="#777"/></svg>Retrip</span></div>
</article>
<article class="card abs" style="left:491px;top:331px;width:130px;height:231px">
  <div class="card-media" style="height:130px;background:linear-gradient(150deg,#8a8f95,#e2e2de 55%,#6c6f72)" role="img" aria-label="Engineers in hard hats reviewing plans on site"></div>
  <div class="card-body"><h3>Rio - Movie</h3><p class="cat">Wallpapers</p><p class="desc">Lorem Ipsum is simply dummy text of the printing &amp; typesetting industry.</p></div>
  <div class="card-foot"><span class="stars">★★★<span>★</span></span><span class="fb"></span><span class="retrip"><svg width="8" height="7" viewBox="0 0 8 7"><rect x="1" y="1" width="6" height="5" fill="none" stroke="#777"/></svg>Retrip</span></div>
</article>

<!-- row 2 -->
<article class="card abs" style="left:70px;top:574px;width:129px;height:228px">
  <div class="card-media" style="height:125px;background:linear-gradient(135deg,#cfd3d8,#7d838b 55%,#3a3e45)" role="img" aria-label="Gloved hands working on a perforated metal part"></div>
  <div class="card-body"><h3>Rio - Movie</h3><p class="cat">Wallpapers</p><p class="desc">Lorem Ipsum is simply dummy text of the printing &amp; typesetting industry.</p></div>
  <div class="card-foot"><span class="stars">★★★<span>★</span></span><span class="fb"></span><span class="retrip"><svg width="8" height="7" viewBox="0 0 8 7"><rect x="1" y="1" width="6" height="5" fill="none" stroke="#777"/></svg>Retrip</span></div>
</article>
<article class="card abs" style="left:210px;top:570px;width:129px;height:183px">
  <div class="card-media" style="height:82px;background:linear-gradient(135deg,#444,#999 50%,#333)" role="img" aria-label="Pile of heavy steel chain"></div>
  <div class="card-body"><h3>Rio - Movie</h3><p class="cat">Movies / Clips</p><p class="desc">Lorem Ipsum is simply dummy text of the printing &amp; typesetting industry.</p></div>
  <div class="card-foot"><span class="stars">★★★<span>★</span></span><span class="fb"></span><span class="retrip"><svg width="8" height="7" viewBox="0 0 8 7"><rect x="1" y="1" width="6" height="5" fill="none" stroke="#777"/></svg>Retrip</span></div>
</article>
<article class="card abs" style="left:350px;top:573px;width:129px;height:225px">
  <div class="card-media" style="height:163px;background:radial-gradient(circle at 50% 45%,#9a7650,#4a3422 65%,#231a12)" role="img" aria-label="Antique clock mechanism with hands"></div>
  <div class="card-body"><h3>Kids movie -Kunfu</h3><p class="cat">Video clips</p></div>
  <div class="card-foot"><span class="stars">★★★<span>★</span></span><span class="fb"></span><span class="retrip"><svg width="8" height="7" viewBox="0 0 8 7"><rect x="1" y="1" width="6" height="5" fill="none" stroke="#777"/></svg>Retrip</span></div>
</article>
<aside class="card followers abs" style="left:491px;top:573px;width:130px;height:195px">
  <h3>Your Followers</h3>
  <div class="follower"><span class="avatar" role="img" aria-label="Follower avatar"></span><div><div class="name">Maren Holt</div><div class="place">Texas</div></div></div>
  <div class="follower"><span class="avatar" role="img" aria-label="Follower avatar"></span><div><div class="name">Dario Pike</div><div class="place">Sentosa west</div></div></div>
  <div class="follower"><span class="avatar" role="img" aria-label="Follower avatar"></span><div><div class="name">Owen Marsh</div><div class="place">Singapore</div></div></div>
  <div class="follower"><span class="avatar" role="img" aria-label="Follower avatar"></span><div><div class="name">Ravi Sandhu</div><div class="place">India</div></div></div>
  <span class="view-all">View all</span>
</aside>

<!-- loading tiles -->
<div class="loading abs" style="left:70px;top:818px;width:129px;height:62px"><svg width="20" height="20" viewBox="-10 -10 20 20"><g stroke-width="3"><line x1="0" y1="-9" x2="0" y2="-4" stroke="#555"/><line x1="6.4" y1="-6.4" x2="2.8" y2="-2.8" stroke="#777"/><line x1="9" y1="0" x2="4" y2="0" stroke="#999"/><line x1="6.4" y1="6.4" x2="2.8" y2="2.8" stroke="#aaa"/><line x1="0" y1="9" x2="0" y2="4" stroke="#bbb"/><line x1="-6.4" y1="6.4" x2="-2.8" y2="2.8" stroke="#ccc"/><line x1="-9" y1="0" x2="-4" y2="0" stroke="#ddd"/><line x1="-6.4" y1="-6.4" x2="-2.8" y2="-2.8" stroke="#e5e5e5"/></g></svg>Loading</div>
<div class="loading abs" style="left:210px;top:770px;width:129px;height:62px"><svg width="20" height="20" viewBox="-10 -10 20 20"><g stroke-width="3"><line x1="0" y1="-9" x2="0" y2="-4" stroke="#555"/><line x1="6.4" y1="-6.4" x2="2.8" y2="-2.8" stroke="#777"/><line x1="9" y1="0" x2="4" y2="0" stroke="#999"/><line x1="6.4" y1="6.4" x2="2.8" y2="2.8" stroke="#aaa"/><line x1="0" y1="9" x2="0" y2="4" stroke="#bbb"/><line x1="-6.4" y1="6.4" x2="-2.8" y2="2.8" stroke="#ccc"/><line x1="-9" y1="0" x2="-4" y2="0" stroke="#ddd"/><line x1="-6.4" y1="-6.4" x2="-2.8" y2="-2.8" stroke="#e5e5e5"/></g></svg>Loading</div>
<div class="loading abs" style="left:350px;top:813px;width:129px;height:62px"><svg width="20" height="20" viewBox="-10 -10 20 20"><g stroke-width="3"><line x1="0" y1="-9" x2="0" y2="-4" stroke="#555"/><line x1="6.4" y1="-6.4" x2="2.8" y2="-2.8" stroke="#777"/><line x1="9" y1="0" x2="4" y2="0" stroke="#999"/><line x1="6.4" y1="6.4" x2="2.8" y2="2.8" stroke="#aaa"/><line x1="0" y1="9" x2="0" y2="4" stroke="#bbb"/><line x1="-6.4" y1="6.4" x2="-2.8" y2="2.8" stroke="#ccc"/><line x1="-9" y1="0" x2="-4" y2="0" stroke="#ddd"/><line x1="-6.4" y1="-6.4" x2="-2.8" y2="-2.8" stroke="#e5e5e5"/></g></svg>Loading</div>
<div class="loading abs" style="left:491px;top:780px;width:130px;height:62px"><svg width="20" height="20" viewBox="-10 -10 20 20"><g stroke-width="3"><line x1="0" y1="-9" x2="0" y2="-4" stroke="#555"/><line x1="6.4" y1="-6.4" x2="2.8" y2="-2.8" stroke="#777"/><line x1="9" y1="0" x2="4" y2="0" stroke="#999"/><line x1="6.4" y1="6.4" x2="2.8" y2="2.8" stroke="#aaa"/><line x1="0" y1="9" x2="0" y2="4" stroke="#bbb"/><line x1="-6.4" y1="6.4" x2="-2.8" y2="2.8" stroke="#ccc"/><line x1="-9" y1="0" x2="-4" y2="0" stroke="#ddd"/><line x1="-6.4" y1="-6.4" x2="-2.8" y2="-2.8" stroke="#e5e5e5"/></g></svg>Loading</div>

<!-- members & partners -->
<section class="band abs"></section>
<h2 class="band-title abs" style="top:914px;font-weight:400">Latest Members</h2>
<div class="carousel abs">
  <svg class="arrow" style="left:16px" width="10" height="16" viewBox="0 0 10 16"><path d="M8 1L2 8l6 7" fill="none" stroke="#c5c9cf" stroke-width="1.5"/></svg>
  <span class="member" style="left:56px;top:9px;width:34px;height:34px;border-radius:50%;background:#e8431e"></span>
  <span class="member" style="left:135px;top:9px;width:110px;height:34px;background:#e8761e"></span>
  <span class="member" style="left:274px;top:11px;width:98px;height:28px;background:#c8102e"></span>
  <span class="member" style="left:406px;top:10px;width:32px;height:32px;background:#b3202f;transform:rotate(45deg)"></span>
  <span class="member" style="left:460px;top:10px;width:36px;height:32px;background:#5b6470"></span>
  <svg class="arrow" style="right:16px" width="10" height="16" viewBox="0 0 10 16"><path d="M2 1l6 7-6 7" fill="none" stroke="#c5c9cf" stroke-width="1.5"/></svg>
</div>
<h2 class="band-title abs" style="top:1003px;font-weight:400">Main Pertners</h2>
<span class="partner" style="left:140px;top:1033px;width:65px"></span>
<span class="partner" style="left:230px;top:1033px;width:75px"></span>
<span class="partner" style="left:333px;top:1033px;width:32px"></span>
<span class="partner" style="left:397px;top:1033px;width:72px"></span>
<span class="partner" style="left:503px;top:1030px;width:47px;height:26px"></span>
<span class="partner" style="left:147px;top:1066px;width:54px"></span>
<span class="partner" style="left:231px;top:1066px;width:66px;background:#b6bcc5"></span>
<span class="partner" style="left:328px;top:1066px;width:100px"></span>
<span class="partner" style="left:454px;top:1066px;width:96px"></span>

<footer class="site-footer abs">
  <p class="stats">MANUFACTURING STATS: 32,000 companies / 600,000 employees<br>The birthplace of the industrial revolution and pioneers in advanced manufacturing</p>
  <nav><span class="current">Home</span><span>Learn More</span><span>News</span><span>Events</span><span>Members</span><span>Annual Expo</span><span>Awards</span><span>Council</span><span>Lobbying</span><span>Team</span><span>Contact Us</span><span>Blog</span><span>Terms &amp; Conditions</span></nav>
</footer>
<div class="bottom-bar abs">
  <span>Copyright@2014, Craft Hollow Works</span><span>|</span><span>Follow Us :</span>
  <span class="social"></span><span class="social"></span><span class="social"></span><span class="social"></span>
</div>

</body>
</html>
```